Torquel Australia Pty Ltd

I require professional business cards with our company logo. We would like something that looks sharp and unique. I have attached the logo for our business, which is an industrial electrical contracting company. But this does not need to be shown on the cards.

Industry/Entity Type

Industrial

Requirements
Must have
• The design must be double sided and needs to have one side with our logo only and the other side with our details.
Should not have
• We do not want any lightening bolts on the designs as this is very common.

```html
<!DOCTYPE html>
<html lang="en">
<head>
<meta charset="utf-8">
<title>Torquel Australia – Business Card</title>
<link rel="stylesheet" href="https://fonts.googleapis.com/css2?family=Source+Sans+3:wght@400;700&family=Arimo:wght@400;700&display=swap">
<style>
  :root {
    --paper: #ffffff;
    --ink: #231f20;
    --gold: #b8965a;
    --gold-soft: #d9c08a;
    --ring: #f1f1f1;
  }
  * { margin: 0; padding: 0; box-sizing: border-box; }
  html, body { width: 1200px; height: 682px; overflow: hidden; background: var(--paper); }
  .card {
    position: relative;
    width: 1200px;
    height: 682px;
    overflow: hidden;
    background: var(--paper);
    color: var(--ink);
  }
  .backdrop-ring {
    position: absolute;
    left: 0; top: 0;
    width: 1200px; height: 682px;
  }
  .brand {
    position: absolute;
    left: 135px;
    top: 106px;
    display: flex;
    align-items: center;
    gap: 16px;
  }
  .brand-dot {
    width: 64px; height: 64px;
    border-radius: 50%;
    background: var(--gold);
  }
  .brand-name {
    font-family: "Source Sans 3", sans-serif;
    font-weight: 700;
    font-size: 40px;
    color: var(--gold);
    line-height: 1;
  }
  .person {
    position: absolute;
    right: 86px;
    top: 44px;
    text-align: right;
    font-family: "Source Sans 3", sans-serif;
    font-weight: 700;
    font-size: 37px;
    line-height: 44px;
  }
  .person-name { color: var(--ink); }
  .person-role { color: var(--gold); }
  .company {
    position: absolute;
    left: 135px;
    top: 406px;
    font-family: "Arimo", sans-serif;
  }
  .company-name { font-weight: 700; font-size: 33px; line-height: 40px; }
  .company-address { font-weight: 400; font-size: 25px; line-height: 32px; }
  .contacts {
    position: absolute;
    left: 135px;
    top: 508px;
    list-style: none;
    font-family: "Arimo", sans-serif;
    font-size: 24px;
    letter-spacing: 1.6px;
  }
  .contact {
    display: flex;
    align-items: center;
    height: 33px;
  }
  .contact-icon {
    width: 20px; height: 20px;
    margin-right: 51px;
    fill: var(--ink);
  }
</style>
</head>
<body>
<div class="card">
  <svg class="backdrop-ring" viewBox="0 0 1200 682" aria-hidden="true">
    <circle cx="852" cy="359" r="318" fill="none" stroke="var(--ring)" stroke-width="34"/>
  </svg>

  <div class="brand">
    <span class="brand-dot"></span>
    <span class="brand-name">Torquel</span>
  </div>

  <div class="person">
    <p class="person-name">Marcus Hale</p>
    <p class="person-role">Director</p>
  </div>

  <div class="company">
    <p class="company-name">Torquel Australia Pty Ltd.</p>
    <p class="company-address">PO Box 318, Camden Park NSW 2570</p>
  </div>

  <ul class="contacts">
    <li class="contact">
      <svg class="contact-icon" viewBox="0 0 20 20" aria-label="Office"><rect x="6" y="2" width="9" height="16" rx="1.5" fill="none" stroke="currentColor" stroke-width="1.6" style="color:var(--ink)"/></svg>
      <span>02 4711 5390</span>
    </li>
    <li class="contact">
      <svg class="contact-icon" viewBox="0 0 20 20" aria-label="Mobile"><path d="M5 3c1-1 2-1 3 0l1.5 2.5c.5 1 0 1.8-.8 2.3-.6.4-.6 1 0 2l1.5 1.8c.8.8 1.3.8 2 .2.8-.7 1.6-.9 2.4-.3l2 1.6c.8.7.8 1.6 0 2.4l-1.2 1.2c-1.5 1.3-5 0-8-3.3C4 10 2.8 6.3 4 4.2z"/></svg>
      <span>0412 730 915</span>
    </li>
    <li class="contact">
      <svg class="contact-icon" viewBox="0 0 20 20" aria-label="Email"><path d="M1 7l9-5 9 5v10H1z"/><path d="M2.5 8l7.5 5 7.5-5" fill="none" stroke="#fff" stroke-width="1.5"/></svg>
      <span>marcus@torquelaustralia.com.au</span>
    </li>
    <li class="contact">
      <svg class="contact-icon" viewBox="0 0 20 20" aria-label="Website"><rect x="1" y="1" width="18" height="18" rx="4"/><circle cx="10" cy="10" r="6" fill="none" stroke="#fff" stroke-width="1.2"/><path d="M4 10h12M10 4v12M10 4c-3 3-3 9 0 12M10 4c3 3 3 9 0 12" fill="none" stroke="#fff" stroke-width="1"/></svg>
      <span>www.torquelaustralia.com.au</span>
    </li>
  </ul>
</div>
</body>
</html>
```